創業130年以上の酢屋です。
国産のりんご果汁だけから造られた「澄実の雫」のラベルデザインを依頼します。
一般のスーパーに卸す商品です。たくさん並ぶ大手さんの「りんご酢」に埋もれない、目を引くデザインをお願いしたいです。
容器は瓶で、スタイリッシュなものではなくごく普通の透明な瓶。お酢は薄い琥珀色です(現在のデザインは画像参照)
国産のりんご果汁100%でできているという点がセールスポイントです。
ターゲットは30代以上の女性。
用途はドレッシング作りやマリネなどの料理、フルーツビネガー等のドリンク作りなどです。
「清潔感」「素朴さ」「丁寧な日常」「かわいらしさ」等、30代以上の女性が好むイメージでデザインしてもらいたいです。

縦に並んだりんごのデザインが大変かわいらしく、中央の商品名、その両脇にあるセールスポイントの文言もはっきりと目立っていました。チラッと見ただけでも印象に残り、年配の方でもはっきり読める大きな文字は、20代~50代のどの従業員さんにも好評でした。手に取ってみると、りんごの中に使用方法や弊社の創業年もあり、お客様に伝えた情報がコンパクトにつまっいてる点も採用のポイントとなりました。

初めて利用しましたが、たくさんのデザイナー様にご提案いただき、感激いたしました。
様々なタイプのデザインの中から選ぶことができたので、これまでのモヤモヤ(本当はこれだ!と思ってないけど、選択肢が二択程度しかなくて、どちらかを選ばざるを得ない)が無く、100%納得の決定ができました。
この後、新商品もすぐに出す予定なのでまた利用したいと思っています。
ご応募いただいた皆様、ほんとうにありがとうございました。
またご縁がありましたら、どうぞよろしくお願い致します。
柏木喜三郎商店(有)
担当:岡部

```html
<!DOCTYPE html>
<html lang="ja">
<head>
<meta charset="utf-8">
<title>澄実の雫 ラベル</title>
<link rel="stylesheet" href="https://fonts.googleapis.com/css2?family=Shippori+Mincho+B1:wght@500;800&family=Cormorant+Garamond:wght@500&display=swap">
<style>
  :root {
    --paper: #efe8da;
    --paper-edge: #e4dccb;
    --ink: #3d3832;
    --ink-soft: #7a7268;
    --apple: #f1b49b;
    --apple-light: #f8d9c9;
    --brand-red: #c23a31;
    --rule: #b9ad98;
  }
  html, body {
    margin: 0;
    padding: 0;
    width: 852px;
    height: 1200px;
    overflow: hidden;
    background: #ffffff;
  }
  .label {
    position: relative;
    width: 852px;
    height: 1200px;
    background: radial-gradient(circle at 50% 40%, #f6f1e6 0%, var(--paper) 55%, var(--paper-edge) 100%);
    font-family: "Shippori Mincho B1", serif;
    color: var(--ink);
  }
  .label__frame {
    position: absolute;
    inset: 24px;
    border: 2px solid var(--rule);
  }
  .category {
    position: absolute;
    top: 62px;
    left: 0;
    width: 100%;
    margin: 0;
    text-align: center;
    font-family: "Cormorant Garamond", serif;
    font-size: 20px;
    letter-spacing: 0.35em;
    color: var(--ink-soft);
  }
  .brand-mark {
    position: absolute;
    top: 52px;
    right: 62px;
    display: flex;
    align-items: center;
    gap: 8px;
    font-size: 26px;
    font-weight: 800;
    color: var(--brand-red);
  }
  .brand-mark__square {
    width: 18px;
    height: 18px;
    background: var(--brand-red);
  }
  .apple-art {
    position: absolute;
    left: 216px;
    top: 340px;
    width: 420px;
    height: 420px;
  }
  .product-name {
    position: absolute;
    left: 50%;
    top: 118px;
    transform: translateX(-50%);
    writing-mode: vertical-rl;
    font-size: 190px;
    font-weight: 800;
    line-height: 1;
    letter-spacing: 0;
    margin: 0;
  }
  .claim {
    position: absolute;
    writing-mode: vertical-rl;
    font-weight: 500;
    margin: 0;
    line-height: 1;
  }
  .claim--origin {
    left: 92px;
    top: 280px;
    font-size: 42px;
    letter-spacing: 0.18em;
  }
  .claim--heritage {
    right: 92px;
    top: 160px;
    font-size: 36px;
    letter-spacing: 0.12em;
  }
  .origin-line {
    position: absolute;
    top: 975px;
    left: 0;
    width: 100%;
    text-align: center;
    font-family: "Cormorant Garamond", serif;
    color: var(--ink);
  }
  .origin-line__place {
    font-size: 30px;
    letter-spacing: 0.18em;
  }
  .origin-line__since {
    margin-top: 8px;
    font-size: 18px;
    letter-spacing: 0.3em;
    color: var(--ink-soft);
  }
</style>
</head>
<body>
  <main class="label">
    <div class="label__frame"></div>

    <p class="category">APPLE CIDER VINEGAR</p>

    <div class="brand-mark">
      <span class="brand-mark__square"></span>
      <span>丸清</span>
    </div>

    <svg class="apple-art" viewBox="0 0 420 420" role="img" aria-label="淡いピーチ色のりんごのイラスト">
      <defs>
        <radialGradient id="appleTone" cx="45%" cy="40%" r="60%">
          <stop offset="0%" stop-color="#f8d9c9"/>
          <stop offset="100%" stop-color="#f1b49b"/>
        </radialGradient>
      </defs>
      <circle cx="210" cy="210" r="200" fill="url(#appleTone)" opacity="0.85"/>
    </svg>

    <h1 class="product-name">澄実の雫</h1>

    <p class="claim claim--origin">国産りんご果汁100%使用</p>
    <p class="claim claim--heritage">創業130年のお酢屋が作った</p>

    <div class="origin-line">
      <div class="origin-line__place">MADE IN SAKURAGAWA</div>
      <div class="origin-line__since">SINCE 1890</div>
    </div>
  </main>
</body>
</html>
```